Divorce marketing brochure - Which will include a toy ball and chain as a gimick

A single page marketing enclosure which includes a toy ball and chain to be given to lawyers. I want to convey the following messages:

1. We pay a 1/3 referral fee;
2. We solve difficult problems.

Examples of problems solved:
*Litigation of complex property, custody, support and parenting time issues;
*Protection (or invasion) of personal injury proceeds in divorce;
*Distribution of consortium proceeds in divorce;
*Pre-nuptial and Post-nuptial agreements.
*Settlements
*Reduce conflict

A sample of the toy ball and chain enclosure can be viewed here:

My website is www.thesplitcounsel.com (currently being updated - who's isn't?)

http://www.shopvarnex.com/Pelbrook-Gadgets-Inc-Convict-Shackle/dp/Q7K4TZ2MXA/ref=sr_1_9?ie=UTF8&qid=1311011554&sr=8-9

Target Market(s)

Personal Injury Attorneys

Industry/Entity Type

Marketing

Requirements
Must have
• Call to action:

www.thesplitcounsel.com
1-866-LAWS-DESK
517-624-8107
Marcus@brevanolegal.com
Nice to have
• I want this campaign to stand out. Different is good. I am a divorce lawyer marketing to personal injury attorneys (and some others) for divorce referrals. (No one forgets the girl with red hair and braces) I want the campaign to be remembered without being offensive.
Should not have

```html
<!DOCTYPE html>
<html lang="en">
<head>
<meta charset="utf-8">
<title>The split counsel – Referral Enclosure</title>
<link rel="stylesheet" href="https://fonts.googleapis.com/css2?family=Oswald:wght@600&family=PT+Sans:wght@400;700&display=swap">
<style>
  :root {
    --bg-top: #cdd6d7;
    --bg-mid: #bcc8c9;
    --bg-low: #c9d2d3;
    --ink-dark: #2b3535;
    --title-ink: #4b5a5a;
    --card-white: #ffffff;
    --panel-light: rgba(230, 236, 236, 0.72);
    --panel-strip: #262d2d;
    --footer-bg: #283030;
    --footer-line: #4a5555;
    --footer-label: #f2f4f4;
    --footer-value: #c9d0d0;
    --edge-black: #111414;
  }
  * { margin: 0; padding: 0; box-sizing: border-box; }
  html, body { width: 1200px; height: 2544px; overflow: hidden; }
  body {
    position: relative;
    background:
      radial-gradient(circle at 1030px 140px, rgba(255,255,255,0.35) 0 150px, transparent 152px),
      radial-gradient(circle at 170px 470px, rgba(255,255,255,0.25) 0 90px, transparent 150px),
      radial-gradient(circle at 1020px 1920px, rgba(255,255,255,0.22) 0 140px, transparent 142px),
      linear-gradient(180deg, var(--bg-top) 0%, var(--bg-mid) 45%, var(--bg-low) 100%);
    font-family: "PT Sans", Arial, sans-serif;
  }
  .top-edge { position: absolute; left: 0; top: 0; width: 1200px; height: 26px; background: var(--edge-black); }
  .name-card {
    position: absolute; left: 242px; top: 0; width: 730px; height: 427px;
    background: var(--card-white);
    border-radius: 0 0 26px 26px;
    box-shadow: 0 4px 0 #7d8a8a, 0 8px 18px rgba(0,0,0,0.18);
    display: flex; align-items: center; justify-content: center;
  }
  .name-card h1 {
    font-family: "PT Sans", Arial, sans-serif; font-weight: 700;
    font-size: 92px; letter-spacing: -2px; color: var(--title-ink);
    margin-top: 8px;
  }
  .pitch {
    position: absolute; left: 164px; top: 520px;
    font-family: "Oswald", "Arial Narrow", sans-serif; font-weight: 600;
    font-size: 64px; line-height: 116px; color: var(--ink-dark);
    letter-spacing: -0.5px;
  }
  .photo-frame {
    position: absolute; left: 96px; top: 829px; width: 1104px; height: 736px;
    background: var(--card-white); padding: 14px 0 14px 14px;
    box-shadow: 0 30px 30px -18px rgba(0,0,0,0.45);
  }
  .photo-fill {
    width: 100%; height: 100%;
    background:
      radial-gradient(ellipse at 55% 40%, #7e958b 0%, #3f5049 45%, #141a18 100%);
  }
  .examples-heading {
    position: absolute; left: 86px; top: 1664px;
    display: flex; align-items: center; gap: 52px;
  }
  .examples-heading .arrow-box {
    width: 58px; height: 48px; background: var(--panel-strip);
    border-radius: 4px; display: flex; align-items: center; justify-content: center;
  }
  .examples-heading h2 {
    font-family: "Oswald", "Arial Narrow", sans-serif; font-weight: 600;
    font-size: 68px; color: #ffffff; letter-spacing: -0.5px;
    text-shadow: 0 2px 4px rgba(0,0,0,0.15);
  }
  .problem-panel {
    position: absolute; left: 86px; top: 1768px; width: 1069px; height: 396px;
    background: var(--panel-light);
    border-left: 58px solid var(--panel-strip);
    padding: 30px 0 0 94px;
  }
  .problem-panel p {
    font-size: 33px; line-height: 45px; color: #1f2626;
    text-shadow: 0 1px 0 rgba(255,255,255,0.6);
  }
  .problem-panel .indent { padding-left: 10px; }
  .problem-panel .indent-2 { padding-left: 20px; }
  .contact-band {
    position: absolute; left: 0; top: 2281px; width: 1200px; height: 263px;
    background: var(--footer-bg); border-top: 4px solid var(--footer-line);
  }
  .contact-list { list-style: none; position: absolute; left: 310px; top: 45px; }
  .contact-list li {
    display: flex; align-items: center; height: 62px;
    font-size: 30px; color: var(--footer-value);
  }
  .contact-list .bullet {
    width: 18px; height: 18px; background: #d9dede; border: 3px solid #8e9999;
    margin-right: 40px;
  }
  .contact-list .label { font-weight: 700; color: var(--footer-label); margin-right: 6px; }
  .contact-list .phone { letter-spacing: 8px; }
  .bottom-edge { position: absolute; left: 0; top: 2519px; width: 1200px; height: 25px; background: var(--edge-black); }
</style>
</head>
<body>
  <div class="top-edge"></div>

  <header class="name-card">
    <h1>The split counsel</h1>
  </header>

  <div class="pitch">
    <div>1. We pay a 1/3 referral fee;</div>
    <div>2. We solve difficult problems.</div>
  </div>

  <figure class="photo-frame">
    <div class="photo-fill" role="img" aria-label="Photograph of a steel ball and chain with an open shackle lying on a dark green-grey floor"></div>
  </figure>

  <div class="examples-heading">
    <span class="arrow-box">
      <svg width="24" height="28" viewBox="0 0 24 28" aria-hidden="true">
        <polyline points="6,4 17,14 6,24" fill="none" stroke="#ffffff" stroke-width="5"/>
      </svg>
    </span>
    <h2>Examples of problems solved:</h2>
  </div>

  <section class="problem-panel">
    <p>*Litigation of complex property, custody,</p>
    <p class="indent">support&nbsp; and parenting time issues;</p>
    <p>*Protection (or invasion) of personal injury</p>
    <p class="indent-2">proceeds in divorce;</p>
    <p>*Distribution of consortium proceeds in divorce;</p>
    <p>*Pre-nuptial and Post-nuptial agreements.</p>
    <p>*Settlements</p>
    <p>*Reduce conflict</p>
  </section>

  <footer class="contact-band">
    <ul class="contact-list">
      <li><span class="bullet"></span><span class="label">CALL ME:</span><span class="phone">517-624-8107</span></li>
      <li><span class="bullet"></span><span class="label">MAIL ME:</span>&nbsp;Marcus@brevanolegal.com</li>
      <li><span class="bullet"></span><span class="label">KNOW US:</span>&nbsp;www.thesplitcounsel.com</li>
    </ul>
  </footer>

  <div class="bottom-edge"></div>
</body>
</html>
```